Velvet Fern Tagline: Beauty & Balance

I’m looking to create a professional website for my body sculpting, facial, waxing, and wellness spa. I’d like clarity on all required components and integrations needed for a fully functional, client‑friendly platform.**

The website should include:

- **Home Page**
- **About Page**
- **Contact Page**
- **Services Page** (with detailed service descriptions)
- **Meet the Team Page**
- **Product Page** (with e‑commerce capabilities)
- **Blog Section** (multiple posts/pages)
**** Education-
- **Refund & Cancellation Policies Page, Legal Polices ( to discuss potient risk when using products and equipment for services rendered *

**Functionality Requirements: **

- Seamless **integration with external platforms** used for scheduling, client management, or marketing.
- Full **e‑commerce capability**, including:
- “Buy Now” Pay Later” solutions like Pay-Lattice, Vorsta, Quillow and Integration with **Tindle Payments** and similar financing providers
- Ability to manage and sell both **services and retail products**.
- A user‑friendly backend for updating content, products, and blog posts.

Technical Requirements
• HIPAA Compliance: Use platforms like Mavrelo or ClinivaHub to ensure client health data and photos are stored securely. HIPAA Notice: Since you offer post-op services, include a small disclaimer below your contact form: "Please do not share sensitive medical information through this form. Private health details will be collected during your secure, HIPAA-compliant intake process".

• Mobile Optimization: Ensure the site is "responsive" so it looks perfect on smartphones where most clients will book.
• SEO: Include local keywords like "Sacramento Body Sculpting" and "Best Waxing in 95731" to help people find you.

I’m seeking guidance on what is required to build this site effectively, including platform recommendations, integrations, and any technical considerations.

Velvet Fern
Tagline : Beauty and Balance

Logo- I created this logo attached. I want this concept but want it revised properly and I am willing to pay for a revised logo which will not be too far off from what you currently see.

Beauty, Cosmetic, Spa, Wellness, Holistic

```html
<!DOCTYPE html>
<html lang="en">
<head>
<meta charset="utf-8">
<title>Velvet Fern — Blog, Education, Contact</title>
<link rel="stylesheet" href="https://fonts.googleapis.com/css2?family=EB+Garamond:wght@400;600&family=Libre+Baskerville:wght@400;700&family=Poppins:wght@400;600&display=swap">
<style>
  :root {
    --plum: #8b1450;
    --pink: #d63c8e;
    --pink-deep: #d6338a;
    --ink: #1c1c1c;
    --body: #333333;
    --line: #d9d9d9;
    --green: #14a06f;
    --footer-pink: #f6d3e4;
    --white: #ffffff;
  }
  * { margin: 0; padding: 0; box-sizing: border-box; }
  html, body { width: 1200px; height: 1200px; overflow: hidden; background: var(--white); }
  body { position: relative; font-family: "Libre Baskerville", Georgia, serif; color: var(--ink); }
  .abs { position: absolute; }
  .copy { font-family: "EB Garamond", Georgia, serif; color: var(--body); }

  .section-title { position: absolute; left: 0; width: 1200px; text-align: center; color: var(--plum); font-weight: 700; }
  .blog-title { top: 18px; font-size: 13px; }
  .contact-title { top: 616px; font-size: 14px; }

  .photo { position: absolute; }
  .blog-card-title { position: absolute; font-size: 9.5px; font-weight: 700; }
  .blog-card-text { position: absolute; width: 116px; font-size: 7.5px; line-height: 12px; }

  .btn { position: absolute; background: var(--pink-deep); color: var(--white); font-size: 9.5px; font-weight: 700;
         display: flex; align-items: center; justify-content: center; }

  .edu-title { left: 407px; top: 414px; font-size: 10.5px; font-weight: 700; }
  .edu-text { left: 407px; top: 432px; width: 128px; font-size: 7.6px; line-height: 11.8px; }
  .edu-list { left: 407px; top: 499px; list-style: none; font-family: "Poppins", Arial, sans-serif; font-size: 6.5px; font-weight: 600; }
  .edu-list li { display: flex; align-items: center; gap: 5px; height: 12px; }
  .edu-shadow { left: 570px; top: 409px; width: 198px; height: 178px; background: var(--pink); }

  .contact-intro { left: 430px; top: 638px; width: 314px; text-align: center; font-size: 7.5px; line-height: 13px; }
  .field-label { position: absolute; font-size: 7.5px; font-weight: 700; }
  .field { position: absolute; border: 1px solid var(--line); border-radius: 3px; background: var(--white); box-shadow: 0 1px 2px rgba(0,0,0,0.06); }

  .footer { left: 326px; top: 1002px; width: 522px; height: 178px; background: linear-gradient(90deg, var(--footer-pink) 0%, #f4d6e6 45%, #e9c9dc 70%, #b9c9d2 100%); overflow: hidden; }
  .footer-art { position: absolute; left: 260px; top: 0; width: 262px; height: 178px;
                background: radial-gradient(ellipse at 70% 40%, rgba(214,80,140,0.45), rgba(140,175,190,0.35) 60%, rgba(246,211,228,0) 100%); }
  .brand { position: absolute; left: 82px; top: 34px; display: flex; align-items: center; gap: 5px; font-size: 9px; font-weight: 700; color: var(--plum); }
  .brand-dot { width: 10px; height: 10px; border-radius: 50%; background: var(--pink); }
  .footer-about { position: absolute; left: 81px; top: 86px; width: 82px; font-size: 6.6px; line-height: 10px; }
  .footer-nav { position: absolute; left: 195px; top: 86px; list-style: none; font-family: "EB Garamond", Georgia, serif; font-size: 6.4px; line-height: 9.2px; color: var(--ink); }
  .footer-nav li:first-child { color: var(--plum); font-weight: 600; }
  .footer-contact-title { position: absolute; left: 268px; top: 88px; font-family: "Poppins", Arial, sans-serif; font-size: 6.5px; color: var(--pink); }
  .footer-contact { position: absolute; left: 268px; top: 106px; list-style: none; font-family: "Poppins", Arial, sans-serif; font-size: 5.6px; color: var(--ink); }
  .footer-contact li { display: flex; align-items: center; gap: 6px; height: 13px; }

  .legal-bar { left: 326px; top: 1180px; width: 522px; height: 20px; background: var(--green); }
  .legal-text { position: absolute; left: 113px; top: 6px; font-family: "Poppins", Arial, sans-serif; font-size: 5.4px; color: var(--white); }
  .social { position: absolute; left: 378px; top: 6px; display: flex; gap: 8px; }
  .social span { width: 7px; height: 7px; border-radius: 50%; background: var(--white); }
</style>
</head>
<body>

  <h2 class="section-title blog-title">Blog</h2>

  <div class="photo" style="left:406px;top:49px;width:114px;height:163px;background:linear-gradient(180deg,#e8e4da,#cfd6cf 55%,#dfe3e6);" role="img" aria-label="Photo of a spa reception desk with staff greeting a client"></div>
  <div class="photo" style="left:529px;top:49px;width:115px;height:76px;background:linear-gradient(135deg,#f0dde4,#c7a9b4 60%,#5b4447);" role="img" aria-label="Photo of a stylist working on a client's hair"></div>
  <div class="photo" style="left:529px;top:139px;width:115px;height:73px;background:linear-gradient(135deg,#5a4a48,#b89686 55%,#e9d2c6);" role="img" aria-label="Photo of a makeup artist applying makeup"></div>
  <div class="photo" style="left:654px;top:49px;width:114px;height:163px;background:linear-gradient(180deg,#ece6ea,#d9c4c9 50%,#e8b3c6);" role="img" aria-label="Photo of a client receiving a hair treatment in a salon chair"></div>

  <h3 class="blog-card-title" style="left:406px;top:224px;">Lorem Ipsum</h3>
  <h3 class="blog-card-title" style="left:529px;top:224px;">Lorem Ipsum</h3>
  <h3 class="blog-card-title" style="left:654px;top:224px;">Lorem Ipsum</h3>

  <p class="blog-card-text copy" style="left:406px;top:245px;">Lorem Ipsum is simply dummy text of the printing and typesetting industry. Lorem Ipsum has been the industry's standard dummy text ever since the 1500s, when an unknown printer took a galley of type and scrambled it to make a type specimen book.</p>
  <p class="blog-card-text copy" style="left:529px;top:245px;">Lorem Ipsum is simply dummy text of the printing and typesetting industry. Lorem Ipsum has been the industry's standard dummy text ever since the 1500s, when an unknown printer took a galley of type and scrambled it to make a type specimen book.</p>
  <p class="blog-card-text copy" style="left:654px;top:245px;">Lorem Ipsum is simply dummy text of the printing and typesetting industry. Lorem Ipsum has been the industry's standard dummy text ever since the 1500s, when an unknown printer took a galley of type and scrambled it to make a type specimen book.</p>

  <div class="btn" style="left:551px;top:342px;width:73px;height:22px;">See Now</div>

  <h3 class="abs edu-title">Education</h3>
  <p class="abs edu-text copy">Lorem Ipsum is simply dummy text of the printing and typesetting industry. Lorem Ipsum has been the industry's standard dummy text ever since the 1500s, specimen book.</p>
  <ul class="abs edu-list">
    <li><svg width="7" height="7" viewBox="0 0 10 10"><path d="M1 5.5 L4 8.5 L9 1.5" fill="none" stroke="#d63c8e" stroke-width="1.6"/></svg>Lorem Ipsum</li>
    <li><svg width="7" height="7" viewBox="0 0 10 10"><path d="M1 5.5 L4 8.5 L9 1.5" fill="none" stroke="#d63c8e" stroke-width="1.6"/></svg>Lorem Ipsum</li>
    <li><svg width="7" height="7" viewBox="0 0 10 10"><path d="M1 5.5 L4 8.5 L9 1.5" fill="none" stroke="#d63c8e" stroke-width="1.6"/></svg>Lorem Ipsum</li>
  </ul>
  <div class="btn" style="left:407px;top:551px;width:73px;height:21px;">See Now</div>

  <div class="abs edu-shadow"></div>
  <div class="photo" style="left:562px;top:401px;width:199px;height:177px;background:linear-gradient(180deg,#1f2224 0%,#2b2d2f 18%,#ef9cbc 19%,#f4a9c5 70%,#ee97b9 100%);" role="img" aria-label="Photo of lash extension tools, tweezers and a mirror on a pink table"></div>

  <h2 class="section-title contact-title">Contact Us</h2>
  <p class="abs contact-intro copy">Lorem Ipsum is simply dummy text of the printing and typesetting industry. Lorem Ipsum has been the industry's standard dummy text ever since the 1500s, when an unknown printer took a galley of type and scrambled it to make a type specimen book.</p>

  <label class="field-label" style="left:407px;top:690px;">Your name *</label>
  <label class="field-label" style="left:592px;top:690px;">Your Phone *</label>
  <div class="field" style="left:407px;top:704px;width:175px;height:27px;"></div>
  <div class="field" style="left:592px;top:704px;width:175px;height:27px;"></div>

  <label class="field-label" style="left:407px;top:740px;">Your Email *</label>
  <div class="field" style="left:407px;top:755px;width:360px;height:26px;"></div>

  <label class="field-label" style="left:407px;top:793px;">How we can help you?</label>
  <div class="field" style="left:407px;top:808px;width:360px;height:117px;"></div>

  <div class="btn" style="left:550px;top:946px;width:74px;height:21px;">Submit</div>

  <footer class="abs footer">
    <div class="footer-art" role="img" aria-label="Soft decorative scene of pink butterflies over a blurred teal background"></div>
    <div class="brand"><span class="brand-dot"></span>Velvet Fern</div>
    <p class="footer-about copy">Lorem Ipsum is simply dummy text of the printing and typesetting industry. Lorem Ipsum has been.</p>
    <ul class="footer-nav">
      <li>HOME</li><li>ABOUT</li><li>SERVICES</li><li>MEET THE TEAM</li><li>PRODUCT</li><li>BLOG</li><li>EDUCATION</li><li>CONTACT</li>
    </ul>
    <div class="footer-contact-title">CONTACT US</div>
    <ul class="footer-contact">
      <li><svg width="7" height="7" viewBox="0 0 10 10"><path d="M2 1 L4 1 L5 3.5 L3.8 4.6 C4.5 6 5.2 6.6 6.4 7.2 L7.5 6 L10 7 L10 9 C5 9.5 0.5 5 1 1 Z" fill="#14a06f"/></svg>+1 916 555 0142</li>
      <li><svg width="7" height="7" viewBox="0 0 10 10"><circle cx="5" cy="5" r="5" fill="#14a06f"/><path d="M3 3 L4.2 3 L4.8 4.3 L4.2 4.9 C4.6 5.6 5 6 5.7 6.3 L6.2 5.7 L7.4 6.2 L7.4 7.2 C5 7.4 2.7 5.2 3 3 Z" fill="#fff"/></svg>+1 916 555 0187 / +1 916 555 0163</li>
      <li><svg width="7" height="7" viewBox="0 0 10 8"><rect x="0" y="0" width="10" height="8" rx="1" fill="#14a06f"/><path d="M0.5 0.8 L5 4.5 L9.5 0.8" fill="none" stroke="#fff" stroke-width="1"/></svg>hello@velvetfernspa.com</li>
      <li><svg width="7" height="7" viewBox="0 0 10 10"><circle cx="5" cy="5" r="5" fill="#14a06f"/><path d="M0.5 5 H9.5 M5 0.5 C2.5 3 2.5 7 5 9.5 M5 0.5 C7.5 3 7.5 7 5 9.5" fill="none" stroke="#fff" stroke-width="0.7"/></svg>www.velvetfernspa.com</li>
    </ul>
  </footer>

  <div class="abs legal-bar">
    <div class="legal-text">Velvet Fern ©. All rights reserved</div>
    <div class="social"><span></span><span></span><span></span><span></span></div>
  </div>

</body>
</html>
```